Business Cards for a small business advisory (business services)

Professional look. Same as would apply for a lawyer, accountant, or other financial services professional. Please use the logo colors

Target Market(s)

small business owners

Industry/Entity Type

Financial Servics

Contact Information for Business Card

Name: Gavin L. Whitmore, CAIA / Title: Business Advisor / Office #: (718) 294-7716 / Mobile #: (917) 382-5047 / Email: g.whitmore@clearfieldventurepartners.example / Web: www.clearfieldventurepartners.example

Font styles to use
Sans Serif

```html
<!DOCTYPE html>
<html lang="en">
<head>
<meta charset="utf-8">
<title>Clearfield Venture Partners – Business Cards</title>
<link rel="stylesheet" href="https://fonts.googleapis.com/css2?family=Arimo:wght@400;700&family=Montserrat:wght@600;700&display=swap">
<style>
  :root {
    --navy: #1b3a6b;
    --green: #8cc63f;
    --ink: #1a1a1a;
    --paper: #ffffff;
    --backdrop: #eceff2;
    --edge: #d9dde2;
  }
  html, body {
    margin: 0;
    padding: 0;
    width: 1200px;
    height: 1200px;
    overflow: hidden;
    background: var(--backdrop);
  }
  .sheet {
    position: relative;
    width: 1200px;
    height: 1200px;
  }
  .card {
    position: absolute;
    left: 172px;
    width: 856px;
    height: 500px;
    background: var(--paper);
    border: 1px solid var(--edge);
    box-sizing: border-box;
  }
  .card--front { top: 85px; }
  .card--back  { top: 631px; }

  /* Front */
  .holder {
    position: absolute;
    right: 66px;
    top: 218px;
    margin: 0;
    font-family: "Arimo", Arial, sans-serif;
    font-weight: 700;
    font-size: 30px;
    color: var(--navy);
    white-space: nowrap;
  }
  .holder__credential {
    font-weight: 400;
    font-size: 20px;
  }
  .contacts {
    position: absolute;
    right: 36px;
    top: 305px;
    margin: 0;
    padding: 0;
    list-style: none;
    font-family: "Arimo", Arial, sans-serif;
    font-size: 21px;
    color: var(--ink);
  }
  .contacts__item {
    display: flex;
    justify-content: flex-end;
    align-items: center;
    height: 33px;
    white-space: nowrap;
  }
  .contacts__icon {
    width: 16px;
    height: 16px;
    margin-left: 14px;
    fill: var(--green);
    flex: none;
  }

  /* Back */
  .brand {
    position: absolute;
    left: 0;
    right: 0;
    top: 200px;
    text-align: center;
    font-family: "Montserrat", Arial, sans-serif;
  }
  .brand__name {
    display: inline-flex;
    align-items: center;
    gap: 18px;
    margin: 0;
    font-weight: 700;
    font-size: 46px;
    color: var(--navy);
    white-space: nowrap;
  }
  .brand__dot {
    width: 34px;
    height: 34px;
    border-radius: 50%;
    background: var(--green);
    flex: none;
  }
  .brand__tagline {
    margin: 14px 0 0;
    font-weight: 600;
    font-size: 14px;
    letter-spacing: 0.4px;
    text-transform: uppercase;
    color: var(--navy);
  }
</style>
</head>
<body>
<main class="sheet">
  <section class="card card--front" aria-label="Card front">
    <h1 class="holder">Gavin L. Whitmore<span class="holder__credential">, CAIA</span></h1>
    <ul class="contacts">
      <li class="contacts__item">(718) 294-7716
        <svg class="contacts__icon" viewBox="0 0 16 16" aria-hidden="true"><path d="M3.6 1.2l2.2 2.4-1.1 1.9c.9 2 2.6 3.7 4.6 4.6l1.9-1.1 2.4 2.2-1 2.4C7.6 13.3 2.7 8.4 1.2 3.4z"/></svg>
      </li>
      <li class="contacts__item">(917) 382-5047
        <svg class="contacts__icon" viewBox="0 0 16 16" aria-hidden="true"><path d="M4.5 1h7v14h-7zM5.8 2.6v9.4h4.4V2.6z"/><circle cx="8" cy="13.4" r=".7" fill="#fff"/></svg>
      </li>
      <li class="contacts__item">g.whitmore@clearfieldventurepartners.example
        <svg class="contacts__icon" viewBox="0 0 16 16" aria-hidden="true"><path d="M1 3.5h14v9H1z"/><path d="M1.5 4l6.5 5 6.5-5" fill="none" stroke="#fff" stroke-width="1.3"/></svg>
      </li>
      <li class="contacts__item">www.clearfieldventurepartners.example
        <svg class="contacts__icon" viewBox="0 0 16 16" aria-hidden="true"><circle cx="8" cy="8" r="7"/><path d="M1.5 8h13M8 1.2c-2.6 3.8-2.6 9.8 0 13.6M8 1.2c2.6 3.8 2.6 9.8 0 13.6" fill="none" stroke="#fff" stroke-width="1"/></svg>
      </li>
    </ul>
  </section>

  <section class="card card--back" aria-label="Card back">
    <div class="brand">
      <p class="brand__name"><span class="brand__dot" aria-hidden="true"></span>Clearfield Venture Partners</p>
      <p class="brand__tagline">Practical guidance for owners ready to buy or sell a business</p>
    </div>
  </section>
</main>
</body>
</html>
```